Want to incorporate elements of all these items to make an amazing sign to welcome people to the community. The sign is 6x4 and needs to incorporate the following items:

Welcome to Corwick Meadows

Come visit the PRD sales center at 745 thistledown road
High Speed Fiber Internet
Land financing starting at $299 (No credit checks)
Let us build your dream home!
555-284-7390
We like the gold and black design no teal or blue that was another agents design. Some combination of the current sign all the stuff listed above and then design elements that tie into the truck wrap.

Target Market(s)

People visiting the neighborhood

Industry/Entity Type

real estate and construction

Font styles to use
Serif

Colors

Designer to choose colors to be used in the design.

Requirements
Must have
• PRD Home Builders Welcomes you to Corwick Meadows, Let us build your dream home, Phone number, Land financing starting at $299 NO credit checks

```html
<!DOCTYPE html>
<html lang="en">
<head>
<meta charset="utf-8">
<title>Welcome to Corwick Meadows</title>
<link rel="stylesheet" href="https://fonts.googleapis.com/css2?family=Inter:wght@400;500;700;800&display=swap">
<style>
  :root {
    --ink: #121314;
    --gold: #a68a46;
    --gold-soft: #9c8243;
    --white: #ffffff;
    --house-roof: #6b6f76;
    --house-wall: #8d8170;
    --house-trim: #e9e2cc;
  }
  * { margin: 0; padding: 0; box-sizing: border-box; }
  html, body { width: 1200px; height: 800px; overflow: hidden; background: var(--ink); }
  .sign {
    position: relative;
    width: 1200px;
    height: 800px;
    background: var(--ink);
    font-family: "Inter", Arial, sans-serif;
    color: var(--white);
    overflow: hidden;
  }
  .sign-art { position: absolute; inset: 0; width: 1200px; height: 800px; }
  .headline {
    position: absolute;
    top: 36px;
    left: 0;
    width: 1200px;
    text-align: center;
    font-size: 60px;
    line-height: 70px;
    letter-spacing: -1px;
    white-space: nowrap;
  }
  .headline-lead { font-weight: 800; color: var(--white); }
  .headline-name { font-weight: 400; color: var(--gold); }
  .feature {
    position: absolute;
    left: 183px;
    font-weight: 700;
    font-size: 32px;
    line-height: 40px;
    letter-spacing: -0.2px;
  }
  .feature-visit { top: 173px; }
  .feature-fiber { top: 320px; }
  .feature-finance { top: 427px; }
  .tagline {
    position: absolute;
    top: 632px;
    left: 0;
    width: 1200px;
    text-align: center;
    font-size: 46px;
    font-weight: 500;
    line-height: 60px;
  }
  .phone {
    position: absolute;
    top: 700px;
    left: 0;
    width: 1200px;
    text-align: center;
    font-size: 64px;
    font-weight: 800;
    line-height: 74px;
    letter-spacing: -1px;
  }
</style>
</head>
<body>
<main class="sign">
  <svg class="sign-art" viewBox="0 0 1200 800" xmlns="http://www.w3.org/2000/svg">
    <defs>
      <linearGradient id="houseTones" x1="0" y1="0" x2="0" y2="1">
        <stop offset="0" stop-color="#6f7680"/>
        <stop offset="0.35" stop-color="#8c8373"/>
        <stop offset="1" stop-color="#9a8f7e"/>
      </linearGradient>
    </defs>

    <path class="house-photo" role="img" aria-label="Photo of a two-storey family home with grey siding, shingled roof and attached garage"
          d="M667,690 L667,455 L672,390 L700,168 L965,180 L1090,88 L1200,150 L1200,690 Z"
          fill="url(#houseTones)"/>

    <polygon class="gold-band" points="0,690 600,535 1200,690 1200,800 0,800" fill="var(--gold)"/>

    <g class="icon icon-sales-center" fill="none" stroke="var(--gold)" stroke-width="2.5">
      <circle cx="112" cy="215" r="45"/>
      <rect x="91" y="193" width="36" height="38"/>
      <line x1="91" y1="199" x2="127" y2="199"/>
      <rect x="96" y="204" width="5" height="6"/><rect x="106" y="204" width="5" height="6"/><rect x="116" y="204" width="5" height="6"/>
      <rect x="96" y="214" width="5" height="6"/><rect x="106" y="214" width="5" height="6"/>
      <path d="M125,213 a7,7 0 0 1 7,7 c0,6 -7,13 -7,13 c0,0 -7,-7 -7,-13 a7,7 0 0 1 7,-7 Z" fill="var(--ink)"/>
      <circle cx="125" cy="220" r="2.5"/>
    </g>

    <g class="icon icon-wifi" fill="none" stroke="var(--gold)" stroke-width="3" stroke-linecap="round">
      <circle cx="112" cy="342" r="45"/>
      <path d="M90,333 a32,32 0 0 1 44,0"/>
      <path d="M97,341 a22,22 0 0 1 30,0"/>
      <path d="M104,349 a12,12 0 0 1 16,0"/>
      <circle cx="112" cy="357" r="2.5" fill="var(--gold)" stroke="none"/>
    </g>

    <g class="icon icon-finance" fill="none" stroke="var(--gold)" stroke-width="2.5">
      <circle cx="112" cy="468" r="45"/>
      <rect x="100" y="446" width="32" height="40" rx="2"/>
      <rect x="105" y="451" width="22" height="7"/>
      <line x1="106" y1="465" x2="126" y2="465"/>
      <line x1="106" y1="472" x2="126" y2="472"/>
      <line x1="106" y1="479" x2="126" y2="479"/>
      <ellipse cx="101" cy="464" rx="9" ry="3" fill="var(--ink)"/>
      <ellipse cx="101" cy="471" rx="9" ry="3" fill="var(--ink)"/>
      <ellipse cx="101" cy="478" rx="9" ry="3" fill="var(--ink)"/>
      <ellipse cx="101" cy="485" rx="9" ry="3" fill="var(--ink)"/>
    </g>
  </svg>

  <h1 class="headline"><span class="headline-lead">WELCOME TO</span> <span class="headline-name">CORWICK MEADOWS</span></h1>

  <p class="feature feature-visit">Come visit the PRD sales<br>center at 745 thistledown road</p>
  <p class="feature feature-fiber">High Speed Fiber Internet</p>
  <p class="feature feature-finance">Land financing starting<br>at $299 (No credit checks)</p>

  <p class="tagline">Let us build your dream home!</p>
  <p class="phone">555-284-7390</p>
</main>
</body>
</html>
```